Oven Cleaning Business owner needs business card design

Hi there,
Would like for a business card to be designed for myself, the owner of a professional oven cleaning business on the Sunshine Coast.
Would like it to look sleek, and modern-ish. Bit creative is encouraged too.
Include following:
Name/title: Corin ter Haghe, Owner
Phone number: 1300 482 916
Email: info@hearthshinecrew.com.au
Website: www.hearthshinecrew.com.au

```html
<!DOCTYPE html>
<html lang="en">
<head>
<meta charset="UTF-8">
<title>Hearthshine Crew – Business Card</title>
<link href="https://fonts.googleapis.com/css2?family=Nunito+Sans:wght@400;600;800&display=swap" rel="stylesheet">
<style>
  :root {
    --teal: #52c3cb;
    --ink: #1a1a1a;
    --paper: #ffffff;
    --backdrop: #e9e7e4;
  }
  * { margin: 0; padding: 0; box-sizing: border-box; }
  html, body { width: 1200px; height: 1200px; overflow: hidden; }
  body {
    background: var(--backdrop);
    font-family: "Nunito Sans", sans-serif;
    position: relative;
  }
  .card {
    position: absolute;
    left: 298px;
    width: 605px;
    height: 345px;
    box-shadow: 0 10px 14px rgba(0,0,0,0.22);
    overflow: hidden;
  }
  .card-front { top: 208px; background: var(--paper); }
  .card-back { top: 675px; background: var(--teal); }

  .front-arc { position: absolute; left: 0; top: 0; }

  .brand {
    position: absolute;
    display: flex;
    align-items: center;
    font-weight: 800;
    text-transform: uppercase;
    letter-spacing: 0.04em;
    line-height: 1.1;
    white-space: nowrap;
  }
  .brand-dot { border-radius: 50%; flex: none; }

  .card-front .brand {
    left: 36px; top: 78px;
    width: 180px;
    flex-direction: column;
    gap: 14px;
    text-align: center;
    color: var(--teal);
    font-size: 22px;
  }
  .card-front .brand-dot { width: 80px; height: 80px; background: var(--teal); }

  .card-back .brand {
    left: 50%; top: 50%;
    transform: translate(-50%, -50%);
    gap: 18px;
    color: var(--paper);
    font-size: 32px;
  }
  .card-back .brand-dot { width: 64px; height: 64px; background: var(--paper); }

  .contact { position: absolute; left: 300px; top: 0; }
  .contact-row {
    position: absolute;
    left: 0;
    display: flex;
    align-items: flex-start;
    gap: 12px;
    color: var(--teal);
    font-size: 18px;
    white-space: nowrap;
  }
  .contact-row svg { flex: none; margin-top: 2px; }
  .contact-name {
    top: 38px;
    font-size: 24px;
    font-weight: 600;
    line-height: 1.28;
  }
  .contact-name svg { margin-top: 4px; }
  .contact-phone { top: 156px; }
  .contact-email { top: 218px; }
  .contact-web { top: 278px; }
</style>
</head>
<body>

<section class="card card-front">
  <svg class="front-arc" width="605" height="345" viewBox="0 0 605 345" aria-hidden="true">
    <path d="M197 0 L220 0 Q 312 170 222 345 L192 345 Q 282 170 197 0 Z" fill="var(--teal)"/>
  </svg>

  <div class="brand">
    <span class="brand-dot"></span>
    <span>Hearthshine<br>Crew</span>
  </div>

  <div class="contact">
    <div class="contact-row contact-name">
      <svg width="20" height="20" viewBox="0 0 20 20" fill="none" stroke="#222" stroke-width="1.5">
        <circle cx="10" cy="6" r="4"/>
        <path d="M2 19 Q2 12 10 12 Q18 12 18 19 Z"/>
      </svg>
      <span>Corin ter Haghe,<br>Owner</span>
    </div>
    <div class="contact-row contact-phone">
      <svg width="22" height="22" viewBox="0 0 24 24" fill="none" stroke="#222" stroke-width="1.5" stroke-linejoin="round">
        <path d="M5 3 L9 3 L10.5 8 L8 9.5 Q10 14 14.5 16 L16 13.5 L21 15 L21 19 Q20 21 17 21 Q4 19 3 6 Q3 3 5 3 Z"/>
      </svg>
      <span>1300 482 916</span>
    </div>
    <div class="contact-row contact-email">
      <svg width="22" height="22" viewBox="0 0 24 24" fill="none" stroke="#222" stroke-width="1.5">
        <rect x="2" y="5" width="20" height="14"/>
        <path d="M2 5 L12 13 L22 5 M2 19 L9 11 M22 19 L15 11"/>
      </svg>
      <span>info@hearthshinecrew.com.au</span>
    </div>
    <div class="contact-row contact-web">
      <svg width="22" height="22" viewBox="0 0 24 24" fill="none" stroke="#222" stroke-width="1.5">
        <circle cx="12" cy="12" r="10"/>
        <ellipse cx="12" cy="12" rx="4.5" ry="10"/>
        <path d="M2 12 H22 M4 7 H20 M4 17 H20"/>
      </svg>
      <span>www.hearthshinecrew.com.au</span>
    </div>
  </div>
</section>

<section class="card card-back">
  <div class="brand">
    <span class="brand-dot"></span>
    <span>Hearthshine Crew</span>
  </div>
</section>

</body>
</html>
```